Business Card Design Project

The logo I included in my order was a previous image that we've used for shirts, signs, magnets, etc. We've decided to go back to that logo, with some updates.
We need to add "Inc." after "Brindell Roofing,"
Also, I need the logo with a transparent background so that I can use it on other projects.

The business cards will be the first item I order with the new logo. The employee's info is:
Derek Palp
Sales Manager
610-743-2956
dpalp@brindellroofinginc.example

Also, I want a "Find us on Chatterbook" icon on the card, along with our web address, www.brindellroofinginc.example.

Any questions, please email or call me:
norabrindell@mailvex.example
610-918-6032

Project Deadline Extended
Reason: This is the first time I've tried Pixel Guild.

My timetable changed and I need to select a design by the end of the work day, 6 hours from now.Thanks so much for all of the super designs.

Target Market(s)

Homeowners

Industry/Entity Type

Business

Font styles to use
Serif

Requirements
Must have
• Transparent background
Similar to logo in photo I sent you

```html
<!DOCTYPE html>
<html lang="en">
<head>
<meta charset="utf-8">
<title>Brindell Roofing Inc. – Business Card</title>
<link rel="stylesheet" href="https://fonts.googleapis.com/css2?family=Noto+Sans:wght@400;500&family=Roboto+Condensed:wght@700&family=Tinos:ital@0;1&display=swap">
<style>
  :root {
    --page: #4a4644;
    --bark: #3b302d;
    --leaf: #76923f;
    --paper: #ffffff;
    --ink: #1c1c1c;
    --sans: "Noto Sans", Arial, sans-serif;
    --serif: "Tinos", "Times New Roman", serif;
    --condensed: "Roboto Condensed", "Arial Narrow", sans-serif;
  }
  * { box-sizing: border-box; margin: 0; padding: 0; }
  html, body { width: 1200px; height: 840px; overflow: hidden; }
  body { background: var(--page); position: relative; }

  .card {
    position: absolute; left: 100px; top: 127px;
    width: 1000px; height: 585px;
    background: var(--bark);
    overflow: hidden;
  }
  .card-shapes { position: absolute; inset: 0; }

  .brand {
    position: absolute; left: 0; width: 450px; top: 186px;
    text-align: center; color: var(--paper); font-family: var(--serif);
  }
  .brand-name { font-size: 31px; line-height: 1.2; }
  .brand-phone { font-size: 28px; line-height: 1.3; }

  .social {
    position: absolute; left: 47px; top: 286px;
    display: flex; align-items: center; gap: 14px; color: var(--paper);
    font-family: var(--sans);
  }
  .social-square { width: 58px; height: 58px; border-radius: 6px; background: var(--paper); }
  .social-label { font-size: 18px; line-height: 1.2; }
  .social-handle { font-size: 25px; line-height: 1.2; }

  .contact {
    position: absolute; right: 50px; top: 96px;
    text-align: right; color: var(--ink); font-family: var(--sans);
  }
  .person-name {
    font-family: var(--condensed); font-weight: 700; color: var(--leaf);
    font-size: 40px; line-height: 1; letter-spacing: 0.5px; margin-right: 34px;
  }
  .person-role { font-size: 24px; margin-top: 8px; margin-right: 34px; }
  .line { display: flex; justify-content: flex-end; align-items: center; gap: 10px; }
  .line svg { width: 24px; height: 24px; flex: none; }
  .phone { font-size: 31px; font-weight: 500; margin-top: 42px; }
  .email, .web { font-size: 22px; margin-top: 10px; }
  .address { font-size: 23px; margin-top: 22px; align-items: flex-start; line-height: 1.5; }
  .address svg { margin-top: 6px; }

  .tagline {
    position: absolute; left: 0; right: 0; top: 476px; height: 109px;
    display: flex; align-items: center; justify-content: center;
    font-family: var(--serif); font-style: italic; font-size: 39px; color: var(--paper);
  }
</style>
</head>
<body>
  <div class="card">
    <svg class="card-shapes" viewBox="0 0 1000 585" aria-hidden="true">
      <polygon points="643,0 709,0 401,412 546,476 498,476 339,427" fill="var(--leaf)"/>
      <polygon points="709,0 1000,0 1000,476 546,476 401,412" fill="var(--paper)"/>
      <rect x="0" y="476" width="1000" height="109" fill="var(--leaf)"/>
    </svg>

    <div class="brand">
      <div class="brand-name">Brindell Roofing Inc.</div>
      <div class="brand-phone">610-555-0148</div>
    </div>

    <div class="social">
      <div class="social-square"></div>
      <div>
        <div class="social-label">Chatterbook</div>
        <div class="social-handle">/brindellroofinginc</div>
      </div>
    </div>

    <div class="contact">
      <div class="person-name">DEREK PALP</div>
      <div class="person-role">Sales Manager</div>
      <div class="line phone">610-743-2956
        <svg viewBox="0 0 24 24"><path fill="var(--leaf)" d="M6.6 3.5l3 3.2-1.8 2.3c1.2 2.6 3.2 4.6 5.8 5.8l2.3-1.8 3.2 3-1.6 3.2C11 18.6 5.4 13 4.8 5.1z"/></svg>
      </div>
      <div class="line email">dpalp@brindellroofinginc.example
        <svg viewBox="0 0 24 24"><rect x="2" y="5" width="20" height="14" fill="var(--leaf)"/><path d="M2.5 5.5l9.5 8 9.5-8" fill="none" stroke="var(--paper)" stroke-width="1.6"/></svg>
      </div>
      <div class="line web">www.brindellroofinginc.example
        <svg viewBox="0 0 24 24" fill="none" stroke="var(--leaf)" stroke-width="1.8"><circle cx="12" cy="12" r="9"/><ellipse cx="12" cy="12" rx="4" ry="9"/><path d="M3 12h18"/></svg>
      </div>
      <div class="line address"><span>482 Ridgeline Road<br>Cedarbrook, PA 18201</span>
        <svg viewBox="0 0 24 24"><path fill="var(--leaf)" d="M12 2a7 7 0 0 0-7 7c0 5 7 13 7 13s7-8 7-13a7 7 0 0 0-7-7zm0 9.5A2.5 2.5 0 1 1 12 6.5a2.5 2.5 0 0 1 0 5z"/></svg>
      </div>
    </div>

    <div class="tagline">Roofing - Siding - Seemless Gutters</div>
  </div>
</body>
</html>
```